BrightHarbor.com Web Site Theme - Home Page/Front Page - Sub-Page theme

Looking for a new site theme that uses tiles like Quellingreport.com but with a unique style. Topbar categories should include following in any particular order w/ pop-out at touch w/ sub-categories (examples below): The main categories for display have an >> prefix . Note main catgories and sub-categories may change.

SPECIAL NOTE: Regional site. We need a way to navigate/drill-down to specific regions on the Central Coast (see the cities accross the top on the current site design)

PORTAL SITE: This site will have a back-end w/ my account and therefore may use a Bootstrap template on the back-end for managing Tiles and articles. Tiles would be the organic content/advertisements on the home page that link to the sub-pages.

TOP BAR CATEGORIES - click to open pop-up w/ sub-categories (some examples in Dining and Real Estate below)

>>Lodging

>>Dining (sub categories below)
Go to Dining >>
Bars & Nightclubs
Lunch & Dinner
Catering
Chinese
Coffee
Italian
Pizza
Seafood
Steakhouse
More >>

>>Wineries

>>Activities & Events

>>Real Estate

>>For Sale (subcategories below)
Auto
Shopping

>>Jobs
..

Target Market(s)

Hotels, Wineries, Restaurants, Tourists

Industry/Entity Type

Real Estate

Coding

Coded - Design and coding required

Number of Pages Required

3 page

Colors
0255a3

Requirements
Must have
• My account (maybe a black bar w/ BH logo accross top w/ My Account, Settings, Login etc)
• Conversion of existing organic content and advertisements to new Tiles platform.
Nice to have
• Kind of a Hybrid between Zorvik.com and QuellingReport.com
• PORTAL THOUGHTS
• If everything were to be thought of as a tile to preview in a 3 column wide format w/ variable heights you can fit articles and sound content mixed in with advertorials.
• Every square tile on BrightHarbor.com could be encapsulated into a “Tile”. The Tile is the preview of the landing page, article, or page.
• Every article, business listings, google map page, etc. can have a Tile associated with it. OR you create a Tile and link it to a URL/page.
• So Tiles become mini snippets of custom HTML that can have 1 or more links etc… Just an HTML Snippet.
• Tile/HTML Snippet
• PreviewTiles.aspx
• Shows all tiles sortable like a product catalog, etc. Additional columns for publishing the tile and where it should reside on the Front Page?
• NEW THEME
• Removal of the traditional BH sidebar and incorporating the triple tile site design. We can still have Tallowmere or a major display as first thing you see above top-bar. The categories can be incorporated into a simple top-bar that on-click you pop-down all subcategories and anything featured. This supports tablets and handhelds instead of the traditional mouse-over...
• Comp Layout (see quellingreport.com)
• 3 columns to 1 column style?
• How to handle mobile devices? (Tiles technique supports Plonko news mobile app - 3 columns PC/Mac browser - 1 column Mobile Phone
• Tile & Page MGT
• How do we convert the existing content pages to our new Tile/Page technique?
• How do we handle advertising Tiles and Tiles embedded on pages?
• Pages
• How is a page handled?
• How are Tiles managed and is that a Page or not?
• How are listings handled and are they defined as a Page?

```html
<!DOCTYPE html>
<html lang="en">
<head>
<meta charset="utf-8">
<title>BrightHarbor.com – Home</title>
<link href="https://fonts.googleapis.com/css2?family=Montserrat:wght@400;500;600;700&family=Roboto+Condensed:wght@700&family=Noto+Serif&family=Arimo&display=swap" rel="stylesheet">
<style>
:root{
  --black:#000;
  --brand-blue:#1a72bd;
  --link-blue:#1e8ee0;
  --orange:#f05a28;
  --yellow:#f7dc3f;
  --green:#8dc63f;
  --slate:#5d6472;
  --panel-grey:#c9c9ca;
  --bar-grey:#e2e3e5;
  --text-grey:#555;
  --white:#fff;
}
*{box-sizing:border-box;margin:0;padding:0}
html,body{width:1200px;height:1190px;overflow:hidden}
body{position:relative;background:var(--slate);font-family:"Montserrat",sans-serif}
.abs{position:absolute}

.site-header{left:0;top:0;width:1200px;height:177px;background:var(--black)}
.brand{left:105px;top:70px;font-weight:600;font-size:34px;color:var(--brand-blue);letter-spacing:-.5px}
.account-links{right:92px;top:44px;font-weight:600;font-size:16px;color:var(--link-blue);word-spacing:4px}
.main-nav{right:75px;top:86px;display:flex;gap:13px;font-family:"Roboto Condensed",sans-serif;font-weight:700;font-size:18px;color:var(--white)}

.hero{left:0;top:177px;width:1200px;height:399px;
  background:linear-gradient(90deg,#3d78b6 0%,#7fa9cf 30%,#dde6e6 48%,#e8e6da 58%,#a9b98f 75%,#4d7338 100%)}
.hero-title{left:0;width:1304px;text-align:center;font-weight:500}
.hero-welcome{top:300px;font-size:31px;color:#555}
.hero-brand{top:333px;font-size:43px;color:var(--brand-blue)}
.hero-cta{left:570px;top:400px;width:181px;height:47px;border-radius:7px;background:var(--orange);color:var(--white);font-weight:700;font-size:19px;display:flex;align-items:center;justify-content:center;letter-spacing:.5px}

.content{left:59px;top:576px;width:1073px;height:518px;background:var(--white)}
.tile-photo{top:609px;width:242px;height:151px}
.tile-title{top:776px;width:242px;text-align:center;color:var(--orange);font-weight:600;font-size:17px}
.tile-text{top:818px;width:242px;text-align:center;color:var(--text-grey);font-weight:600;font-size:11px;line-height:15.7px}

.events{left:873px;top:606px;width:236px;height:286px;background:var(--panel-grey)}
.events-head{height:53px;background:var(--brand-blue);color:var(--white);font-weight:500;font-size:21px;display:flex;align-items:center;justify-content:center}
.events-text{padding:19px 14px 0;text-align:center;color:var(--text-grey);font-weight:600;font-size:13.2px;line-height:15.8px}
.btn-yellow{width:172px;background:var(--yellow);border-radius:8px;display:flex;align-items:center;justify-content:center;text-align:center;font-weight:500;font-size:17px;color:#111;line-height:24px}

.newsletter{left:81px;top:940px;width:766px;height:101px;background:var(--bar-grey)}
.newsletter-label{left:124px;top:986px;font-family:"Noto Serif",serif;font-size:18px;color:var(--brand-blue)}
.newsletter-input{left:256px;top:973px;width:265px;height:43px;background:var(--white);border-radius:8px;padding:12px 13px;font-size:15px;color:#777}
.newsletter-submit{left:538px;top:976px;width:126px;height:40px;background:var(--green);border-radius:5px;color:var(--white);font-weight:600;font-size:16px;display:flex;align-items:center;justify-content:center}

.site-footer{left:102px;top:1116px;font-family:"Arimo",sans-serif;font-size:13px;color:var(--white);line-height:21px}
.social{left:961px;top:1125px;display:flex;gap:23px}
.social span{width:18px;height:18px;border-radius:50%;background:#9aa0ab}
</style>
</head>
<body>
<header class="site-header abs">
  <div class="brand abs">BrightHarbor.com</div>
  <div class="account-links abs">Login &nbsp;I&nbsp; My Account</div>
  <nav class="main-nav abs">
    <span>Home</span><span>Lodging</span><span>Dining</span><span>Wineries</span><span>Activities &amp; Events</span><span>Real Estate</span><span>For Sale</span><span>Jobs</span>
  </nav>
</header>

<section class="hero abs" role="img" aria-label="Aerial photo of a curving sandy beach with ocean waves and green hills at sunrise"></section>
<div class="hero-title hero-welcome abs">Welcome to</div>
<div class="hero-title hero-brand abs">BrightHarbor</div>
<div class="hero-cta abs">LEARN MORE</div>

<main class="content abs"></main>

<div class="tile-photo abs" style="left:83px;background:linear-gradient(180deg,#7fb0de,#9cc6e6 60%,#3f6f9a)" role="img" aria-label="Photo of a traveller by the sea"></div>
<div class="tile-title abs" style="left:83px">Location 1</div>
<div class="tile-text abs" style="left:83px">Lorem ipsum dolor sit amet, con-<br>sectetuer adipiscing elit, sed diam<br>nonummy nibh euismod tincidunt<br>ut laoreet dolore magna aliquam<br>erat volutpat.</div>

<div class="tile-photo abs" style="left:346px;background:linear-gradient(110deg,#e6825a,#f6d3bb 55%,#fdf3e8)" role="img" aria-label="Photo of a hiker in hazy sunlight"></div>
<div class="tile-title abs" style="left:346px">Location 2</div>
<div class="tile-text abs" style="left:346px">Lorem ipsum dolor sit amet, con-<br>sectetuer adipiscing elit, sed diam<br>nonummy nibh euismod tincidunt<br>ut laoreet dolore magna aliquam<br>erat volutpat.</div>

<div class="tile-photo abs" style="left:599px;background:linear-gradient(90deg,#8a9563,#c9c7c4 55%,#f4f4f4)" role="img" aria-label="Photo of a backpacker overlooking a misty landscape"></div>
<div class="tile-title abs" style="left:599px">Location 3</div>
<div class="tile-text abs" style="left:599px">Lorem ipsum dolor sit amet, con-<br>sectetuer adipiscing elit, sed diam<br>nonummy nibh euismod tincidunt<br>ut laoreet dolore magna aliquam<br>erat volutpat.</div>

<aside class="events abs">
  <div class="events-head">Activities/Events</div>
  <p class="events-text">Lorem ipsum dolor sit amet, consectetuer adipiscing elit, sed diam nonummy nibh euis-mod tincidunt ut laoreet dolore magna aliquam erat volutpat.&nbsp; nibh euismod tinci-dunt ut laoreet</p>
</aside>
<div class="btn-yellow abs" style="left:903px;top:818px;height:51px">learn more</div>
<div class="btn-yellow abs" style="left:903px;top:944px;height:80px">Find our<br>Locations</div>

<section class="newsletter abs"></section>
<div class="newsletter-label abs">Newsletter</div>
<div class="newsletter-input abs">your email</div>
<div class="newsletter-submit abs">Sign up</div>

<footer class="site-footer abs">
  © 2015 BrightHarbor<br>
  Home - Site Map – FAQ – Privacy Policy – Terms of Use – Contact Us
</footer>
<div class="social abs" aria-label="Social links"><span></span><span></span><span></span><span></span></div>
</body>
</html>
```